120ml Jar Label — Masculine Cosmetic Foot Balm for Cracked, Hardworking Heels

We need a print-ready wraparound label for a 120ml jar — a brown/amber glass jar with a black metal screw lid (file photo attached).

--DO NOT PUT A BARCODE ON THE LABEL PLEASE--
**PLEASE READ "PLAN HUDDLE PROJECT BRIEF FINAL.MD" IN ATTACHED FILES IF YOU ARE SUBMITTING A DESIGN.**

The label is 190mm wide × 40mm high.
We need files to be in an .ai format with a 2mm bleed at the end.
Social media handle: @bramblekeepnz (facebook, instagram and tiktok)

Bramble Keep is a New Zealand foot-care brand making practical, no-nonsense products for hardworking men whose jobs wreck their feet. Our flagship product, Ridge Mender Balm, helps fix thick, cracked, hardworking skin.

Brand color scheme and overview is all in the brief file. You may add some brand aligned colors outside of the specified hex codes as you see fit to make a great design. Feel free to remove the "Bramble Keep" text from the logo so Bramble Keep is not doubled up on the front of the label

The tone we want: direct, rugged, and credible — like a workwear brand, not a spa brand. Most cracked-heel products on the market lean soft and feminine; we want to stand apart by looking like a serious fix for a real problem, made in New Zealand.

Full legal requirements for New Zealand cosmetic labelling (ingredients, directions, net contents, origin, etc.) are listed in the attached brief document — these are non-negotiable and must stay legible.

Please see the label attached "Label spacing guide" for this project's rough spacing guide. This label is the same size and sits well on the jar. This label doesn't need to be spaced quite as much as the Verin Label

I want to run the design for a week - I feel 7 days is a good amount of time for designers to see the work, digest the brief and create something remarkable and memorable for Bramble Keep.

Target Market(s)

Working men in New Zealand whose jobs or lifestyle put heavy wear on their feet — tradies, farmers, hospital/shift workers, hunters, and outdoors people. Practical, value-driven buyers rather than luxury skincare shoppers.

Industry/Entity Type

Beauty / Health & Wellness / Cosmetics

Font styles to use
Sans Serif
Other font styles liked:
• Montserrat (bold, headings), Inter (regular, body)

Colors
00AB8E
00BBA5
67D7C9
C6EFE9
E9F9F6
FFC000
F8CF3A
FAE287
FDF2CF
FEFAEE

Requirements
Must have
• All NZ cosmetic labelling requirements from the attached brief (product name, tag line, net contents, ingredients, directions, storage, made in NZ) — legible and complete, not omitted for aesthetics Fits 190mm × 40mm wraparound format for a 120ml brown jar with black lid Uses our existing brand colors: Deep Olive #3C4A34, Bone White #F4EFE6, Terracotta Clay #C1683D, and Warm Grey #4A4540 (exact palette in attached brief) Uses Montserrat (headings) and Inter (body) or close equivalents Incorporates our existing shield-and-wing logo (attached) Brand name and product name clearly readable from a normal shelf/bathroom-cabinet distance
Nice to have
• A style that could extend into a hero/product photo later, similar to the NZ-hills-backdrop look on our website (screenshot attached) — not required for the label itself, just good to keep in mind Original icon work (e.g. a small soak/apply/sock icon set) if it fits the rugged brand feel A design that could work as a small back-label/wraparound split if the front can't fit everything at a readable size
Should not have
• No pastel colors, floral motifs, or delicate script fonts — this should never look like spa/luxury skincare. Don't introduce new brand colors outside the palette provided other than black.

```html
<!DOCTYPE html>
<html lang="en">
<head>
<meta charset="utf-8">
<title>Bramble Keep – Ridge Mender Balm Label</title>
<link rel="stylesheet" href="https://fonts.googleapis.com/css2?family=Inter:wght@400;600&family=Montserrat:wght@600;700&display=swap">
<style>
  :root {
    --page: #e6e5e3;
    --olive: #3c4a34;
    --olive-light: #55634b;
    --bone: #f4efe6;
    --clay: #c1683d;
    --sage: #93a287;
  }
  * { box-sizing: border-box; margin: 0; padding: 0; }
  html, body { width: 1200px; height: 800px; overflow: hidden; }
  body {
    background: var(--page);
    font-family: "Inter", Arial, sans-serif;
    color: var(--bone);
    position: relative;
  }
  .jar-label {
    position: absolute;
    left: 54px;
    top: 285px;
    width: 1092px;
    height: 229px;
    background: var(--olive);
    border-top: 6px solid var(--clay);
    border-bottom: 7px solid var(--clay);
  }
  .panel-heading {
    font-weight: 600;
    font-size: 12.5px;
    letter-spacing: 0.1px;
    margin-bottom: 6px;
  }
  .panel-text {
    font-size: 12.5px;
    line-height: 16.2px;
  }
  .directions {
    position: absolute;
    left: 30px;
    top: 38px;
    width: 290px;
  }
  .storage { margin-top: 18px; }
  .foot-art {
    position: absolute;
    left: 314px;
    top: 0;
    width: 160px;
    height: 112px;
    background: radial-gradient(ellipse at 45% 45%, var(--olive-light) 0%, rgba(85,99,75,0.4) 55%, rgba(60,74,52,0) 80%);
    opacity: 0.8;
  }
  .brand-block {
    position: absolute;
    left: 446px;
    top: 16px;
    width: 200px;
    text-align: center;
  }
  .brand-mark {
    width: 46px;
    height: 46px;
    border-radius: 50%;
    background: var(--bone);
    margin: 0 auto 10px;
  }
  .brand-name {
    font-family: "Montserrat", Arial, sans-serif;
    font-weight: 700;
    font-size: 14px;
    color: var(--bone);
    letter-spacing: 0.5px;
  }
  .product-name {
    font-family: "Montserrat", Arial, sans-serif;
    font-weight: 700;
    font-size: 21px;
    color: var(--bone);
    margin-top: 20px;
    letter-spacing: 0.3px;
    white-space: nowrap;
  }
  .tagline {
    font-family: "Montserrat", Arial, sans-serif;
    font-weight: 600;
    font-size: 14.5px;
    color: var(--clay);
    margin-top: 1px;
  }
  .net-contents {
    font-family: "Montserrat", Arial, sans-serif;
    font-weight: 600;
    font-size: 11.5px;
    color: var(--sage);
    margin-top: 22px;
  }
  .origin {
    position: absolute;
    left: 714px;
    top: 60px;
    width: 16px;
    height: 138px;
    font-size: 11.5px;
    color: var(--sage);
    letter-spacing: 0.3px;
    writing-mode: vertical-rl;
    transform: rotate(180deg);
    white-space: nowrap;
    text-align: left;
  }
  .ingredients {
    position: absolute;
    left: 784px;
    top: 38px;
    width: 268px;
  }
  .website {
    position: absolute;
    left: 784px;
    top: 188px;
    font-family: "Montserrat", Arial, sans-serif;
    font-weight: 600;
    font-size: 14.5px;
    color: var(--clay);
  }
</style>
</head>
<body>
  <section class="jar-label" aria-label="Ridge Mender Balm jar label">
    <div class="directions">
      <h2 class="panel-heading">DIRECTIONS:</h2>
      <p class="panel-text">Apply generously to clean, dry feet, focusing on heels and thick or cracked areas. For cracked heels, wear our moisture-locking socks overnight. Use daily.</p>
      <h2 class="panel-heading storage">STORAGE:</h2>
      <p class="panel-text">Keep out of direct sunlight. Best used within six months of opening.</p>
    </div>

    <div class="foot-art" role="img" aria-label="Faint illustration of a bare foot and ankle"></div>

    <div class="brand-block">
      <div class="brand-mark"></div>
      <p class="brand-name">BRAMBLE KEEP</p>
      <h1 class="product-name">RIDGE MENDER BALM</h1>
      <p class="tagline">For Hardworking Soles</p>
      <p class="net-contents">120ML</p>
    </div>

    <p class="origin">MADE IN NEW ZEALAND</p>

    <div class="ingredients">
      <h2 class="panel-heading">INGREDIENTS:</h2>
      <p class="panel-text">Shea Butter, Beef Tallow, Beeswax, Grape Seed Oil, Vegetable Glycerin, Lanolin, Panthenol, Gluconolactone &amp; Sodium Benzoate, Manuka Honey, Allantoin, Vitamin E, Tea Tree Essential Oil, Lemon Myrtle Essential Oil, Rosemary Oleoresin Extract.</p>
    </div>

    <p class="website">www.bramblekeep.com</p>
  </section>
</body>
</html>
```